Bolt Ridge Hoist Service Business Cards

I need a business card for "Bolt Ridge Hoist and Tackle"

Boltridge2023@hoistmail.example

Hoist Works LLC, Bolt Ridge Hoist and Tackle LLC

555.204.7186 | www.BOLTRIDGEHOISTS.example

Central Indiana & Northeast Ohio

(IN) 23810 Meadow Lane Noblesville, IN 46099

(OH) 4150 Dunmore Street Akron, Ohio 44397

Contact Information for Business Card

Colors
0094D4
00A9DD
6FCCEA
C7EBF8
E9F6FB
59FF00
82FF00
B8FF75
E3FFCB
F4FFEA
EE7325
F08F49
F5BC92
FAE3D3
FDF4ED
EB3D1F
EC4F4E
F09395
F8D3D4
FCEDEE
E54698
E96AAD
F1A4CE
F9D9EA
FCEFF6
A7469A
B969AE
D3A5CF
EDDBEB
F8F0F9

```html
<!DOCTYPE html>
<html lang="en">
<head>
<meta charset="utf-8">
<title>Bolt Ridge Hoist Service Business Cards</title>
<link rel="stylesheet" href="https://fonts.googleapis.com/css2?family=Lato:ital,wght@0,300;0,400;0,900;1,300&display=swap">
<style>
  :root {
    --stage: #121212;
    --card: #1f1f1f;
    --green: #3cb44a;
    --white: #ffffff;
    --grey: #cfcfcf;
    --red: #eb3d1f;
  }
  * { box-sizing: border-box; margin: 0; padding: 0; }
  html, body { width: 1200px; height: 1156px; overflow: hidden; background: var(--stage); }
  body { font-family: "Lato", sans-serif; display: flex; flex-direction: column; align-items: center; justify-content: center; gap: 42px; }
  .card { position: relative; width: 900px; height: 514px; background: var(--card); overflow: hidden; }

  /* contact side */
  .person { position: absolute; left: 64px; top: 78px; width: 380px; }
  .person-name { color: var(--green); font-weight: 900; font-size: 38px; line-height: 1.1; letter-spacing: 1px; text-transform: uppercase; white-space: nowrap; }
  .person-role { color: var(--grey); font-weight: 300; font-size: 22px; margin-top: 4px; }
  .brand { position: absolute; right: 64px; top: 66px; width: 360px; display: flex; align-items: flex-start; justify-content: flex-end; gap: 14px; }
  .brand-mark { width: 18px; height: 18px; margin-top: 10px; background: var(--green); flex: none; }
  .brand-name { color: var(--white); font-weight: 900; font-size: 36px; line-height: 1.1; text-transform: uppercase; text-align: right; white-space: nowrap; }
  .divider { position: absolute; left: 64px; right: 64px; top: 206px; height: 3px; background: var(--green); }
  .contacts { position: absolute; left: 64px; top: 232px; list-style: none; }
  .contacts li { display: flex; align-items: center; gap: 12px; color: var(--grey); font-weight: 300; font-size: 21px; line-height: 36px; }
  .contacts svg { width: 18px; height: 18px; fill: var(--green); flex: none; }
  .addresses { position: absolute; right: 64px; bottom: 52px; list-style: none; }
  .addresses li { display: flex; align-items: center; gap: 12px; color: var(--grey); font-weight: 300; font-size: 21px; line-height: 34px; }
  .addresses svg { width: 16px; height: 20px; fill: var(--green); flex: none; }

  /* logo side */
  .crane-art { position: absolute; right: 50px; top: 24px; width: 240px; height: 430px;
    background: linear-gradient(160deg, #1a1a1a 0%, #0b0b0b 45%, #2f8f3a 100%); border-radius: 6px; }
  .lockup { position: absolute; left: 70px; top: 160px; width: 500px; }
  .lockup-name { color: var(--white); font-weight: 900; font-size: 46px; line-height: 1.08; text-transform: uppercase; white-space: nowrap; }
  .legal-band { display: inline-block; margin-top: 24px; background: var(--red); color: var(--white); font-weight: 900; font-size: 15px; letter-spacing: .4px; text-transform: uppercase; padding: 9px 16px; white-space: nowrap; }
</style>
</head>
<body>

<section class="card card-contact">
  <div class="person">
    <p class="person-name">Dana Whitcombe</p>
    <p class="person-role">Owner</p>
  </div>
  <div class="brand">
    <span class="brand-mark"></span>
    <p class="brand-name">Bolt Ridge<br>Hoist &amp; Tackle</p>
  </div>
  <div class="divider"></div>
  <ul class="contacts">
    <li><svg viewBox="0 0 24 24"><path d="M6.6 10.8a15 15 0 0 0 6.6 6.6l2.2-2.2a1 1 0 0 1 1-.25 11.4 11.4 0 0 0 3.6.57 1 1 0 0 1 1 1V20a1 1 0 0 1-1 1A17 17 0 0 1 3 4a1 1 0 0 1 1-1h3.5a1 1 0 0 1 1 1c0 1.25.2 2.45.57 3.57a1 1 0 0 1-.25 1z"/></svg>555.204.7186</li>
    <li><svg viewBox="0 0 24 24"><path d="M2 5h20v14H2z M2 5l10 8 10-8" fill="none" stroke="#3cb44a" stroke-width="2"/></svg>Boltridge2023@hoistmail.example</li>
    <li><svg viewBox="0 0 24 24"><circle cx="12" cy="12" r="9" fill="none" stroke="#3cb44a" stroke-width="2"/><path d="M3 12h18M12 3c3 3 3 15 0 18M12 3c-3 3-3 15 0 18" fill="none" stroke="#3cb44a" stroke-width="1.6"/></svg>www.boltridgehoists.example</li>
  </ul>
  <ul class="addresses">
    <li><svg viewBox="0 0 20 26"><path d="M10 0a9 9 0 0 0-9 9c0 7 9 17 9 17s9-10 9-17a9 9 0 0 0-9-9zm0 13a4 4 0 1 1 0-8 4 4 0 0 1 0 8z"/></svg>(IN) 23810 Meadow Lane Noblesville, IN 46099</li>
    <li><svg viewBox="0 0 20 26"><path d="M10 0a9 9 0 0 0-9 9c0 7 9 17 9 17s9-10 9-17a9 9 0 0 0-9-9zm0 13a4 4 0 1 1 0-8 4 4 0 0 1 0 8z"/></svg>(OH) 4150 Dunmore Street Akron, Ohio 44397</li>
  </ul>
</section>

<section class="card card-logo">
  <div class="crane-art" role="img" aria-label="Illustration of a green and black mobile crane with raised boom and hoist lines"></div>
  <div class="lockup">
    <p class="lockup-name">Bolt Ridge<br>Hoist and Tackle</p>
    <p class="legal-band">Hoist Works LLC, Bolt Ridge Hoist and Tackle LLC</p>
  </div>
</section>

</body>
</html>
```